Medical Marijuana Service in the Bay Area

This is for a business card design that is going to be making medical marijuana deliveries in the bay area. The name of the the business is "Coastal Sage Wellness". I would like to have a modern feel and showing us as a medical marijuana company but at the same time discrete about it. I'm trying to target more sophisticated clients.

Industry/Entity Type

Medical

Contact Information for Business Card

Would like people to know it is for medical marijuana but in a discrete way.

```html
<!DOCTYPE html>
<html lang="en">
<head>
<meta charset="utf-8">
<title>Coastal Sage Wellness – Business Card</title>
<link rel="stylesheet" href="https://fonts.googleapis.com/css2?family=PT+Sans:wght@400&display=swap">
<style>
  :root {
    --backdrop: #2e2e2e;
    --card-white: #ffffff;
    --navy: #232f3a;
    --sage: #7dbd4f;
    --ink-light: #e6e9ec;
    --rule: #7a8590;
  }
  * { margin: 0; padding: 0; box-sizing: border-box; }
  html, body {
    width: 1200px;
    height: 441px;
    overflow: hidden;
    background: var(--backdrop);
    font-family: "PT Sans", sans-serif;
  }
  .canvas { position: relative; width: 1200px; height: 441px; }

  .card {
    position: absolute;
    top: 59px;
    width: 507px;
    height: 307px;
    border-radius: 14px;
    overflow: hidden;
    background: var(--card-white);
  }
  .card--front { left: 103px; }
  .card--back { left: 633px; }

  /* brand lockup */
  .brand { position: absolute; text-align: center; color: var(--navy); }
  .brand__mark {
    display: block;
    width: 40px;
    height: 40px;
    margin: 0 auto 18px;
    background: var(--sage);
    border-radius: 6px;
  }
  .brand__name { font-size: 22px; letter-spacing: 0.5px; white-space: nowrap; }

  .card--front .brand { left: 0; width: 507px; top: 102px; }

  .web-bar {
    position: absolute;
    left: 169px;
    top: 269px;
    width: 174px;
    height: 22px;
    background: var(--sage);
    color: var(--navy);
    font-size: 11.5px;
    line-height: 22px;
    text-align: center;
  }

  /* back */
  .back-wave { position: absolute; left: 0; top: 0; width: 507px; height: 307px; }
  .card--back .brand { right: 22px; width: 230px; top: 30px; }
  .card--back .brand__mark { width: 36px; height: 36px; margin-bottom: 16px; }
  .card--back .brand__name { font-size: 20px; }

  .contact-list {
    position: absolute;
    left: 28px;
    top: 180px;
    list-style: none;
    color: var(--ink-light);
    font-size: 12.5px;
  }
  .contact-list li { display: flex; align-items: flex-start; height: 27px; }
  .contact-list li.contact--address { line-height: 16px; }
  .contact-list svg { width: 13px; height: 13px; margin: 2px 12px 0 0; flex: none; }

  .person {
    position: absolute;
    left: 307px;
    top: 225px;
    width: 182px;
    padding: 0 0 4px 12px;
    border-bottom: 1px solid var(--rule);
    color: var(--ink-light);
    font-size: 28px;
    white-space: nowrap;
  }
</style>
</head>
<body>
<main class="canvas">

  <section class="card card--front">
    <div class="brand">
      <span class="brand__mark"></span>
      <span class="brand__name">Coastal Sage Wellness</span>
    </div>
    <div class="web-bar">www.coastalsagewellness.com</div>
  </section>

  <section class="card card--back">
    <svg class="back-wave" viewBox="0 0 507 307" aria-hidden="true">
      <path d="M0,66 C120,148 300,178 507,180 L507,190 C300,188 110,164 0,80 Z" fill="var(--sage)"/>
      <path d="M0,80 C110,164 300,188 507,190 L507,307 L0,307 Z" fill="var(--navy)"/>
    </svg>

    <div class="brand">
      <span class="brand__mark"></span>
      <span class="brand__name">Coastal Sage Wellness</span>
    </div>

    <ul class="contact-list">
      <li>
        <svg viewBox="0 0 13 13"><rect x="3.5" y="0.5" width="6" height="12" rx="1.2" fill="none" stroke="var(--sage)" stroke-width="1.2"/><circle cx="6.5" cy="10.5" r="0.8" fill="var(--sage)"/></svg>
        415-000 555 0142
      </li>
      <li>
        <svg viewBox="0 0 13 13"><rect x="0.6" y="2.6" width="11.8" height="8" fill="none" stroke="var(--sage)" stroke-width="1.2"/><path d="M0.6,2.6 L6.5,7.2 L12.4,2.6" fill="none" stroke="var(--sage)" stroke-width="1.2"/></svg>
        hello@coastalsagewellness.com
      </li>
      <li>
        <svg viewBox="0 0 13 13"><circle cx="6.5" cy="6.5" r="5.8" fill="none" stroke="var(--sage)" stroke-width="1.1"/><ellipse cx="6.5" cy="6.5" rx="2.6" ry="5.8" fill="none" stroke="var(--sage)" stroke-width="1"/><path d="M0.7,6.5 H12.3 M1.6,3.6 H11.4 M1.6,9.4 H11.4" stroke="var(--sage)" stroke-width="0.9"/></svg>
        www.coastalsagewellness.com
      </li>
      <li class="contact--address">
        <svg viewBox="0 0 13 13"><path d="M1,6.5 L6.5,1.2 L12,6.5" fill="none" stroke="var(--sage)" stroke-width="1.3"/><path d="M2.6,5.4 V12 H5.3 V8.4 H7.7 V12 H10.4 V5.4" fill="none" stroke="var(--sage)" stroke-width="1.2"/></svg>
        <span>88 Harbor Lane, Suite 210, Bayview,<br>CA 94107 , USA</span>
      </li>
    </ul>

    <div class="person">Daniel Reyes</div>
  </section>

</main>
</body>
</html>
```